Packaging Design Project for Snack product

we are manufacturer banana chips and potato based snacks.our company name is "velmora Foods" and,looking a packaging design for our new product "Potato Twirlies" under brand name " Munchlo".

we need nice colour scheme and wording on the front and back.just a little more professional looking with the wow factor to help it stand out on the shelve.

so pls find below information about the design:
Company name: Velmora Foods
Brand name : Munchlo
Product name : Potato Twirlies
Flavored : Sweet & Spicy
Package Size : 40 GM and 100 GM

Target Market(s)

Retail Customers

Industry/Entity Type

It Company

Requirements
Must have
• In this design we need small visible part for display our product.

```html
<!DOCTYPE html>
<html lang="en">
<head>
<meta charset="utf-8">
<title>Munchlo Potato Twirlies – Pack Fronts</title>
<link rel="stylesheet" href="https://fonts.googleapis.com/css2?family=Oswald:wght@400;700&family=Russo+One&display=swap">
<style>
  :root {
    --stage: #f2f2f2;
    --white: #ffffff;
    --window-light: #d3d7da;
    --window-dark: #a9b0b4;

    --red-top: #e3001f;
    --red-bottom: #a8091a;
    --red-soft: #ef1d36;
    --red-band: #111111;
    --red-brand: #ffffff;

    --yellow-top: #fff000;
    --yellow-bottom: #f9b233;
    --yellow-soft: #fff55a;
    --yellow-band: #5b3311;
    --yellow-brand: #5b3311;
  }

  html, body {
    margin: 0;
    padding: 0;
    width: 1200px;
    height: 788px;
    overflow: hidden;
    background: var(--stage);
  }

  .stage {
    position: relative;
    width: 1200px;
    height: 788px;
    background: var(--stage);
  }

  .pack {
    position: absolute;
    top: 76px;
    width: 461px;
    height: 653px;
  }
  .pack--red    { left: 122px; --bag-top: var(--red-top); --bag-bottom: var(--red-bottom); --bag-soft: var(--red-soft); --band: var(--red-band); --brand: var(--red-brand); }
  .pack--yellow { left: 636px; --bag-top: var(--yellow-top); --bag-bottom: var(--yellow-bottom); --bag-soft: var(--yellow-soft); --band: var(--yellow-band); --brand: var(--yellow-brand); }

  .pack svg { display: block; width: 100%; height: 100%; }

  .stop-top    { stop-color: var(--bag-top); }
  .stop-bottom { stop-color: var(--bag-bottom); }
  .stop-window-light { stop-color: var(--window-light); }
  .stop-window-dark  { stop-color: var(--window-dark); }

  .crimp { fill: var(--white); opacity: 0.45; }
  .soft-area { fill: var(--bag-soft); opacity: 0.55; }
  .band-dark { fill: none; stroke: var(--band); stroke-linecap: round; }
  .band-white { fill: none; stroke: var(--white); stroke-linecap: round; }
  .window-edge { stroke: var(--white); stroke-width: 6; }

  .product-title {
    font-family: "Russo One", sans-serif;
    font-size: 56px;
    fill: var(--white);
  }

  .brand-name {
    font-family: "Oswald", sans-serif;
    font-weight: 400;
    font-size: 30px;
    letter-spacing: 1px;
    fill: var(--brand);
  }
  .flavour {
    font-family: "Oswald", sans-serif;
    font-weight: 700;
    font-size: 13px;
    fill: var(--white);
  }
  .net-weight {
    font-family: "Oswald", sans-serif;
    font-weight: 400;
    font-size: 17px;
    letter-spacing: 1px;
    fill: var(--white);
  }
</style>
</head>
<body>
<main class="stage">

  <section class="pack pack--red" aria-label="Munchlo Potato Twirlies, red pack">
    <svg viewBox="0 0 395 560" xmlns="http://www.w3.org/2000/svg">
      <defs>
        <linearGradient id="bag-fill-red" x1="0" y1="0" x2="0" y2="1">
          <stop offset="0" class="stop-top"/>
          <stop offset="1" class="stop-bottom"/>
        </linearGradient>
        <linearGradient id="window-fill-red" x1="0" y1="0" x2="1" y2="0">
          <stop offset="0" class="stop-window-light"/>
          <stop offset="1" class="stop-window-dark"/>
        </linearGradient>
      </defs>

      <rect class="bag-body" x="0" y="0" width="395" height="560" fill="url(#bag-fill-red)"/>

      <g class="crimp-top">
        <rect class="crimp" x="0" y="2" width="395" height="1.6"/>
        <rect class="crimp" x="0" y="6" width="395" height="1.6"/>
        <rect class="crimp" x="0" y="10" width="395" height="1.6"/>
      </g>
      <g class="crimp-bottom">
        <rect class="crimp" x="0" y="547" width="395" height="1.6"/>
        <rect class="crimp" x="0" y="551" width="395" height="1.6"/>
        <rect class="crimp" x="0" y="555" width="395" height="1.6"/>
      </g>

      <g class="swoosh-top-left">
        <path class="band-dark" stroke-width="10" d="M0,28 Q100,32 168,112"/>
        <path class="band-white" stroke-width="3" d="M0,17 Q110,20 180,104"/>
      </g>

      <g class="brand-arc">
        <path class="soft-area" d="M205,12 C215,90 320,118 395,58 L395,12 Z"/>
        <path class="band-dark" stroke-width="8" d="M200,14 C212,102 330,132 395,66"/>
        <path class="band-white" stroke-width="3" d="M205,12 C215,90 320,118 395,58"/>
      </g>

      <g class="product-window">
        <path class="band-dark" stroke-width="10" d="M395,137 C300,158 226,260 230,360 C234,452 302,522 395,545"/>
        <path class="window-edge" role="img" aria-label="Clear window showing the potato twirlies inside" fill="url(#window-fill-red)" d="M395,150 C310,170 245,265 248,360 C252,445 315,510 395,530 Z"/>
      </g>

      <g class="weight-arc">
        <path class="soft-area" d="M15,548 C60,455 215,435 280,548 Z"/>
        <path class="band-dark" stroke-width="7" d="M22,548 C66,462 212,444 274,548"/>
        <path class="band-white" stroke-width="3" d="M12,546 C58,450 218,430 284,546"/>
      </g>

      <g class="product-title">
        <text x="36" y="190" textLength="215" lengthAdjust="spacingAndGlyphs">POTATO</text>
        <text x="28" y="255" textLength="200" lengthAdjust="spacingAndGlyphs">TWIRLIES</text>
      </g>

      <text class="brand-name" x="295" y="72" text-anchor="middle">MUNCHLO</text>
      <text class="flavour" x="128" y="292" text-anchor="middle">Sweet &amp; Spicy</text>
      <text class="net-weight" x="148" y="515" text-anchor="middle">100 GM</text>
    </svg>
  </section>

  <section class="pack pack--yellow" aria-label="Munchlo Potato Twirlies, yellow pack">
    <svg viewBox="0 0 395 560" xmlns="http://www.w3.org/2000/svg">
      <defs>
        <linearGradient id="bag-fill-yellow" x1="0" y1="0" x2="0" y2="1">
          <stop offset="0" class="stop-top"/>
          <stop offset="1" class="stop-bottom"/>
        </linearGradient>
        <linearGradient id="window-fill-yellow" x1="0" y1="0" x2="1" y2="0">
          <stop offset="0" class="stop-window-light"/>
          <stop offset="1" class="stop-window-dark"/>
        </linearGradient>
      </defs>

      <rect class="bag-body" x="0" y="0" width="395" height="560" fill="url(#bag-fill-yellow)"/>

      <g class="crimp-top">
        <rect class="crimp" x="0" y="2" width="395" height="1.6"/>
        <rect class="crimp" x="0" y="6" width="395" height="1.6"/>
        <rect class="crimp" x="0" y="10" width="395" height="1.6"/>
      </g>
      <g class="crimp-bottom">
        <rect class="crimp" x="0" y="547" width="395" height="1.6"/>
        <rect class="crimp" x="0" y="551" width="395" height="1.6"/>
        <rect class="crimp" x="0" y="555" width="395" height="1.6"/>
      </g>

      <g class="swoosh-top-left">
        <path class="band-dark" stroke-width="10" d="M0,28 Q100,32 168,112"/>
        <path class="band-white" stroke-width="3" d="M0,17 Q110,20 180,104"/>
      </g>

      <g class="brand-arc">
        <path class="soft-area" d="M205,12 C215,90 320,118 395,58 L395,12 Z"/>
        <path class="band-dark" stroke-width="8" d="M200,14 C212,102 330,132 395,66"/>
        <path class="band-white" stroke-width="3" d="M205,12 C215,90 320,118 395,58"/>
      </g>

      <g class="product-window">
        <path class="band-dark" stroke-width="10" d="M395,137 C300,158 226,260 230,360 C234,452 302,522 395,545"/>
        <path class="window-edge" role="img" aria-label="Clear window showing the potato twirlies inside" fill="url(#window-fill-yellow)" d="M395,150 C310,170 245,265 248,360 C252,445 315,510 395,530 Z"/>
      </g>

      <g class="weight-arc">
        <path class="soft-area" d="M15,548 C60,455 215,435 280,548 Z"/>
        <path class="band-dark" stroke-width="7" d="M22,548 C66,462 212,444 274,548"/>
        <path class="band-white" stroke-width="3" d="M12,546 C58,450 218,430 284,546"/>
      </g>

      <g class="product-title">
        <text x="36" y="190" textLength="215" lengthAdjust="spacingAndGlyphs">POTATO</text>
        <text x="28" y="255" textLength="200" lengthAdjust="spacingAndGlyphs">TWIRLIES</text>
      </g>

      <text class="brand-name" x="295" y="72" text-anchor="middle">MUNCHLO</text>
      <text class="flavour" x="128" y="292" text-anchor="middle">Sweet &amp; Spicy</text>
      <text class="net-weight" x="148" y="515" text-anchor="middle">100 GM</text>
    </svg>
  </section>

</main>
</body>
</html>
```